New Website for ReBranded Company - CrewBeacon

We have a successful company and website currently but it is a little dated. We have re-branded the company from Harbor Signal Networks to CrewBeacon and have a new logo for the new name. We are looking to build a newer fresher website with the new name. I will need a concept of the home page and one inside page. You can see our current site at https://www.harborsignalnetworks.example and the new site will be https://www.crewbeacon.example .

I also really like the https://www.pathmolder.example/ website. I like ledgerleaf.example website. I like the https://skillbinder.example/ website.

See the attached document for layout and some text to use. Use the pictures I attached as opposed to pictures from the old site as much as you can.

Target Market(s)

Business

Industry/Entity Type

Software Service

Number of Pages Required

2 page

Font styles to use
Sans Serif

Requirements
Must have
• Use the colors from my logo. Professional but modern. We want people to feel like our product makes their staff feel safer at work.
Should not have
• Don't use any red or orange (no stop colors).

```html
<!DOCTYPE html>
<html lang="en">
<head>
<meta charset="utf-8">
<title>CrewBeacon – Home</title>
<link rel="stylesheet" href="https://fonts.googleapis.com/css2?family=Nunito+Sans:wght@400;600;700;800;900&family=Lato:wght@300;400;700&display=swap">
<style>
:root{
  --navy:#0d2238;
  --blue:#2f8fd6;
  --blue-soft:#5aaee3;
  --blue-deep:#0b4f86;
  --green:#6cbf3c;
  --green-dark:#4fa630;
  --ice:#e3f0fa;
  --paper:#f7f7f7;
  --white:#ffffff;
  --ink:#2a2f36;
  --muted:#7b8591;
  --stage:#eef0f3;
}
*{box-sizing:border-box;margin:0;padding:0}
html,body{width:1200px;height:3016px;overflow:hidden}
body{background:var(--stage);font-family:"Lato",sans-serif;color:var(--ink);position:relative}
.page{position:absolute;left:56px;top:54px;width:1084px;height:2908px;background:var(--white);box-shadow:0 18px 50px rgba(20,40,70,.16);overflow:hidden}
section,header,footer{position:relative;width:100%}
.abs{position:absolute}
.h2{font-family:"Nunito Sans",sans-serif;font-weight:900;color:var(--navy);font-size:21px;line-height:26px;letter-spacing:.3px;text-transform:uppercase;text-align:center}
.btn{position:absolute;display:flex;align-items:center;justify-content:center;border-radius:22px;font-family:"Nunito Sans",sans-serif;font-weight:700;font-size:12px;color:var(--white)}
.btn-green{background:var(--green);box-shadow:0 6px 14px rgba(108,191,60,.35)}
.btn-blue{background:var(--blue);box-shadow:0 6px 14px rgba(47,143,214,.35)}
.btn-white{background:var(--white);color:var(--navy)}

/* header */
.site-header{height:76px;background:var(--white)}
.brand{left:76px;top:22px;display:flex;align-items:center;gap:8px}
.brand-dot{width:30px;height:30px;border-radius:50%;background:var(--blue)}
.brand-name{font-family:"Nunito Sans",sans-serif;font-weight:700;font-size:22px;color:var(--blue)}
.nav a{position:absolute;top:33px;font-family:"Nunito Sans",sans-serif;font-size:9px;font-weight:600;color:#3a4656;text-decoration:none;letter-spacing:.2px}
.header-cta{left:845px;top:20px;width:158px;height:36px;background:linear-gradient(90deg,var(--green),var(--blue))}

/* hero */
.hero{height:533px;background:linear-gradient(120deg,#58524b 0%,#8b7a68 38%,#7f8a74 62%,#b9c2ae 100%)}
.hero-shade{inset:0;background:linear-gradient(90deg,rgba(20,24,28,.55),rgba(20,24,28,0) 60%)}
.hero-title{left:78px;top:104px;font-family:"Nunito Sans",sans-serif;font-weight:900;font-size:36px;line-height:41px;color:var(--white);text-transform:uppercase}
.hero-sub{left:79px;top:248px;font-size:13px;color:var(--white)}
.hero-cta{left:79px;top:286px;width:166px;height:38px}
.strip{left:173px;top:444px;display:flex;height:89px}
.strip div{padding:20px 26px;color:#e9f4fd;font-size:11.5px;line-height:17px;font-weight:300}
.strip .a{width:252px;background:var(--blue)}
.strip .b{width:234px;background:var(--blue-soft)}
.strip .c{width:252px;background:var(--blue)}

/* problem */
.problem{height:346px;background:var(--paper)}
.problem .h2{position:absolute;left:0;right:0;top:87px}
.problem p{position:absolute;left:0;right:0;top:154px;text-align:center;font-size:13px;line-height:19px;color:var(--ink)}
.problem .btn{left:459px;top:221px;width:165px;height:41px}

/* why */
.why{height:528px;background:linear-gradient(115deg,#0e3a63 0%,#175d92 45%,#0f4a7a 75%,#0a3457 100%)}
.why .h2{position:absolute;left:0;right:0;top:64px;color:var(--white)}
.why-card{position:absolute;top:124px;width:208px;height:270px;background:var(--white);text-align:center;padding:46px 18px 0}
.why-card.featured{background:linear-gradient(180deg,#1f6ea8,#114a78);color:var(--white)}
.why-card h3{font-family:"Lato",sans-serif;font-weight:400;font-size:12px;line-height:18px;text-transform:uppercase;margin-top:20px;color:#3a4350}
.why-card.featured h3{color:var(--white)}
.why-card p{font-size:9px;line-height:14px;margin-top:10px;color:var(--muted)}
.why-card.featured p{color:#e6f1fb}
.opt{display:grid;grid-template-columns:76px 60px;justify-content:center;text-align:left;font-size:8px;line-height:12px;color:var(--muted);margin-top:6px}
.why .btn{left:459px;top:437px;width:165px;height:41px}

/* reassure */
.reassure{height:433px;background:var(--ice)}
.reassure .h2{position:absolute;left:0;right:0;top:84px}
.r-card{position:absolute;top:174px;width:321px;height:156px;background:var(--white);box-shadow:0 4px 12px rgba(30,70,110,.06)}
.r-art{position:absolute;left:40px;top:40px;width:68px;height:70px;border-radius:6px}
.r-card p{position:absolute;left:136px;top:40px;width:170px;font-family:"Nunito Sans",sans-serif;font-weight:600;font-size:11px;line-height:15px;color:var(--navy)}
.r-card .btn{left:136px;top:108px;width:73px;height:24px;font-size:8px;font-weight:400}

/* plan */
.plan{height:553px;background:var(--white)}
.plan .h2{position:absolute;left:0;right:0;top:77px}
.plan-card{position:absolute;top:156px;width:208px;height:250px;background:var(--white);box-shadow:0 6px 18px rgba(30,50,80,.08)}
.plan-photo{height:119px;background:linear-gradient(135deg,#3b3a3c,#7b6d5f 45%,#c9c1b6)}
.plan-card h4{margin:16px 22px 0;padding-bottom:10px;height:48px;border-bottom:1px solid #e6e8eb;font-family:"Nunito Sans",sans-serif;font-weight:600;font-size:11px;line-height:15px;color:#3a4350}
.plan-card ul{list-style:none;margin:10px 22px;font-size:10px;line-height:16px;color:var(--muted)}
.plan-card p{margin:10px 16px 0 22px;font-size:10px;line-height:16px;color:var(--muted)}
.plan .btn{left:476px;top:441px;width:131px;height:41px}

/* cta band */
.cta-band{height:140px;background:var(--ice)}
.cta-band .h2{position:absolute;left:206px;top:54px;text-align:left}
.cta-band .btn{left:769px;top:50px;width:131px;height:41px}

/* footer */
.site-footer{height:299px;background:var(--white)}
.col{position:absolute;top:49px;font-size:8.5px;line-height:12px;color:var(--muted)}
.col h5{font-weight:400;font-size:8.5px;text-transform:uppercase;margin-bottom:14px;color:var(--muted)}
.col a{display:block;color:#4678a6;text-decoration:none;margin-bottom:12px}
.col .phone{display:flex;align-items:center;gap:8px;color:#3a4350;margin-bottom:8px}
.col .blurb{width:140px;font-size:7.5px;line-height:11px}
.foot-brand{left:211px;top:198px;display:flex;align-items:center;gap:6px}
.foot-brand .brand-dot{width:24px;height:24px}
.foot-brand .brand-name{font-size:15px}
.socials{left:212px;top:242px;display:flex;gap:7px}
.socials span{width:7px;height:7px;border-radius:50%;background:#4a5563}
.newsletter{left:719px;top:85px;width:152px;height:29px;display:flex;box-shadow:0 3px 10px rgba(0,0,0,.08)}
.newsletter .field{flex:1;display:flex;align-items:center;padding-left:20px;font-size:7.5px;color:var(--muted)}
.newsletter .go{width:35px;background:var(--green);display:flex;align-items:center;justify-content:center}
.copy{left:211px;top:274px;font-size:7px;color:var(--muted)}
</style>
</head>
<body>
<div class="page">

  <header class="site-header">
    <div class="abs brand"><span class="brand-dot"></span><span class="brand-name">CrewBeacon</span></div>
    <nav class="nav">
      <a style="left:538px">HOME</a>
      <a style="left:613px">BUY ADD-ONS</a>
      <a style="left:723px">CUSTOMER LOG IN</a>
    </nav>
    <a class="btn header-cta">Explore Your Choices</a>
  </header>

  <section class="hero" role="img" aria-label="Hand pressing a wireless panic button mounted under a desk">
    <div class="abs hero-shade"></div>
    <h1 class="abs hero-title">Feel confident<br>that your staff is<br>protected</h1>
    <p class="abs hero-sub">Get a revolutionary new Electronic Panic Button</p>
    <a class="btn btn-green hero-cta">Ready To Get Started</a>
    <div class="abs strip">
      <div class="a">Problems Stopped Before They Start For Any Type Of Organization</div>
      <div class="b">Affordable Prices Starting at $18 per month. No Contracts. No Hidden Costs.</div>
      <div class="c">Alerts by computer, mobile device, text, phone, email, monitoring and E911</div>
    </div>
  </section>

  <section class="problem">
    <h2 class="h2">Your empoyees shouldn’t feel alone when<br>they need help</h2>
    <p>Does this problem make you feel frustrated and anxious?<br>Put a simple solution in their hands</p>
    <a class="btn btn-green">Ready To Get Started</a>
  </section>

  <section class="why" role="img" aria-label="Blue-tinted office desk phone in the background">
    <h2 class="h2">Why businesses choose us?</h2>
    <div class="why-card featured" style="left:212px">
      <svg width="60" height="58" viewBox="0 0 60 58" fill="none" stroke="#fff" stroke-width="2"><circle cx="26" cy="26" r="12"/><path d="M12 52c2-10 26-10 28 0"/><path d="M14 26a12 12 0 0 1 24 0"/><rect x="38" y="4" width="18" height="12" rx="2"/><path d="M42 10h10"/></svg>
      <h3>Easy to use</h3>
      <p>Press a button and let the right people know you need help and open a chat window letting everyone talk on resolving their problem.</p>
    </div>
    <div class="why-card" style="left:437px">
      <svg width="60" height="58" viewBox="0 0 60 58" fill="none" stroke="#6cbf3c" stroke-width="2.4"><path d="M10 36V28a20 20 0 0 1 40 0v8"/><rect x="6" y="34" width="10" height="18" rx="4"/><rect x="44" y="34" width="10" height="18" rx="4"/><path d="M22 26a11 11 0 0 1 16 0M26 31a5 5 0 0 1 8 0"/></svg>
      <h3>Communicate the way<br>you want</h3>
      <p>We give you lots of options:</p>
      <div class="opt"><span>Computer<br>Mobile<br>Email<br>Phone call</span><span>Text<br>E911<br>Call Center</span></div>
    </div>
    <div class="why-card" style="left:663px">
      <svg width="60" height="58" viewBox="0 0 60 58" fill="none" stroke="#6cbf3c" stroke-width="2.4"><path d="M16 44a12 12 0 0 1 2-24 14 14 0 0 1 26 2 10 10 0 0 1 0 22z"/><rect x="22" y="28" width="16" height="12" rx="2"/><path d="M25 28v-4a5 5 0 0 1 10 0v4"/></svg>
      <h3>Cost effective<br>protection</h3>
      <p>Alerts by computer, mobile device, text, phone, email, monitoring and E911</p>
    </div>
    <a class="btn btn-white">Ready To Get Started</a>
  </section>

  <section class="reassure">
    <h2 class="h2">Your empoyees shouldn’t feel alone when<br>they need help</h2>
    <div class="r-card" style="left:206px">
      <div class="r-art" role="img" aria-label="Illustration of a factory worker at a control desk" style="background:linear-gradient(135deg,#3a6fd8,#f2c14e)"></div>
      <p>We know how scary it can feel to worry about employee safety.</p>
      <a class="btn btn-blue">Start Trial</a>
    </div>
    <div class="r-card" style="left:556px">
      <div class="r-art" role="img" aria-label="Illustration of a safe holding a coin" style="background:linear-gradient(135deg,#2f8fd6,#f2c14e)"></div>
      <p style="top:46px">That’s why we have provided a way for customers to get help to staff effectively in <b>45 States</b> covering <b>5 Countries</b></p>
    </div>
  </section>

  <section class="plan">
    <h2 class="h2">Simple start plan</h2>
    <div class="plan-card" style="left:183px">
      <div class="plan-photo" role="img" aria-label="Team meeting around a laptop"></div>
      <h4>Explore Your Choices</h4>
      <ul><li>• Pricing</li><li>• Trial</li><li>• Quote</li><li>• Hardware</li></ul>
    </div>
    <div class="plan-card" style="left:437px">
      <div class="plan-photo" role="img" aria-label="Team meeting around a laptop"></div>
      <h4>Get Setup</h4>
      <ul><li>• Input Your Alerts</li><li>• Input Your Staff</li><li>• Install Our Software</li></ul>
    </div>
    <div class="plan-card" style="left:691px">
      <div class="plan-photo" role="img" aria-label="Team meeting around a laptop"></div>
      <h4>Feel Confident Your Staff Is Protected</h4>
      <p>High Five. You just too a major step to getting rid of the anxiety and frustration this gave you.</p>
    </div>
    <a class="btn btn-blue">Start My Demo</a>
  </section>

  <section class="cta-band">
    <h2 class="h2">Stay connected with staff during<br>a crisis situation</h2>
    <a class="btn btn-blue">Start My Demo</a>
  </section>

  <footer class="site-footer">
    <div class="col" style="left:211px">
      <h5 style="text-transform:none">Contact</h5>
      <div class="phone"><svg width="9" height="9" viewBox="0 0 10 10" fill="none" stroke="#7b8591"><path d="M2 1l2 2-1 1.5a6 6 0 0 0 2.5 2.5L7 6l2 2-1.5 1.5C4 9 1 6 .5 2.5z"/></svg>+1 – 800 – 555 – 0142</div>
      <p class="blurb">When employees feel alone during a threatening situation, we give them a way to let the right resources know that they need help so you can feel confident that your staff is protected.</p>
    </div>
    <div class="abs foot-brand"><span class="brand-dot"></span><span class="brand-name">CrewBeacon</span></div>
    <div class="abs socials"><span></span><span></span><span></span><span></span></div>
    <div class="col" style="left:381px"><h5>Shop</h5><a>Add Ons</a><a>Start My Demo</a><a>Custom Quote</a><a>Start Trial</a></div>
    <div class="col" style="left:494px"><h5>About</h5><a>Affiliates</a><a>Contact</a><a>Support</a><a>Existing Customers</a><a>Industries</a><a>Blog</a><a>FAQ</a></div>
    <div class="col" style="left:607px"><h5>Legal</h5><a>Privacy Policy</a><a>Terms of Use</a><a>End User License</a><a>Agreement</a></div>
    <div class="col" style="left:719px"><h5 style="text-transform:none">Sign up for monthly newsletter</h5></div>
    <div class="abs newsletter">
      <div class="field">@&nbsp;&nbsp;&nbsp;Email</div>
      <div class="go"><svg width="14" height="14" viewBox="0 0 14 14" fill="none" stroke="#fff" stroke-width="1.3"><path d="M13 1L1 6l5 2 2 5z M13 1L6 8"/></svg></div>
    </div>
    <p class="abs copy">© CrewBeacon 2020 All rights reserved</p>
  </footer>

</div>
</body>
</html>
```